Harbison Projects Promo Brochure

Design a simple ,visually impactful brochure that will articulate our company experience and services to prospective clients.

We need to project to have the following elements / structure:
1. Company Intro
2. Company Services
3. Experience
4. Contact Info
5. Images

I'd like to use icons and imagery as needed to illustrate services and experience.
This brochure will be emailed, so the final version will need to be compressed.

I've uploaded our Owner Rep Services, which has phasing, and services (within each phase), see attached. This info needs to be cleanly added to a brochure.

The "Why Harbison Building Management" doc, copy, needs to be included in the brochure.

Include contact info:
Harbison Projects Services, LLC
214-555-0193
www.harbisonprojgroup.example

Target Market(s)

Restaurants and Hospitality Concepts

Font styles to use
Sans Serif

Colors

Designer to choose colors to be used in the design.

Requirements
Must have
• Very easy to read. Clean.
Information and images should be balanced nicely on the page.

use colors of our logo: red, black, grey, white
Should not have
• Very busy text or images.

```html
<!DOCTYPE html>
<html lang="en">
<head>
<meta charset="utf-8">
<title>Harbison Projects Promo Brochure</title>
<link href="https://fonts.googleapis.com/css2?family=Montserrat:wght@400;500;600;700;800&display=swap" rel="stylesheet">
<style>
:root{
  --stage:#3a3b3e;
  --ink:#17181a;
  --ink-soft:#232427;
  --red:#d8232a;
  --red-dark:#a3161c;
  --grey:#8d8f94;
  --grey-light:#e6e7e9;
  --white:#ffffff;
  --phase-green:#3f9a4a;
  --phase-blue:#2f6fb3;
  --phase-orange:#e0892b;
  --phase-red:#c8232a;
}
*{box-sizing:border-box;margin:0;padding:0}
html,body{width:845px;height:1200px;overflow:hidden}
body{background:var(--stage);font-family:"Montserrat",sans-serif;color:var(--white);position:relative}
.spread{position:absolute;left:32px;width:780px;height:552px;display:flex;box-shadow:0 10px 30px rgba(0,0,0,.45)}
.spread--cover{top:24px}
.spread--inner{top:624px}
.page{position:relative;width:390px;height:552px;overflow:hidden}

/* brand lockup */
.brand{display:flex;align-items:center;gap:8px}
.brand__mark{width:22px;height:22px;background:var(--red);flex:none}
.brand__name{font-weight:700;font-size:13px;letter-spacing:.5px;text-transform:uppercase;color:var(--white)}
.brand--dark .brand__name{color:var(--ink)}

/* back cover */
.back-cover{background:var(--ink)}
.back-cover__photo{position:absolute;left:0;top:0;width:390px;height:250px;background:linear-gradient(180deg,#4a4038 0%,#2a2725 60%,var(--ink) 100%);opacity:.8}
.back-cover__body{position:absolute;left:70px;top:270px}
.back-cover__contact{margin-top:14px;font-size:9px;line-height:1.6;color:var(--grey-light)}

/* front cover */
.front-cover{background:var(--ink-soft)}
.front-cover__brand{position:absolute;left:150px;top:70px;flex-direction:column;align-items:flex-start}
.front-cover__brand .brand__mark{width:40px;height:40px}
.front-cover__shape{position:absolute;left:0;top:0}
.front-cover__web{position:absolute;bottom:18px;right:24px;font-size:8px;color:var(--white);letter-spacing:.5px}

/* inner left */
.services{background:var(--white);color:var(--ink);padding:22px 20px}
.services__head{display:flex;align-items:center;gap:10px;border-bottom:3px solid var(--red);padding-bottom:10px}
.services__title{font-size:11px;font-weight:700;color:var(--red);line-height:1.3}
.phase-table{width:100%;border-collapse:collapse;margin-top:14px;font-size:7px;line-height:1.35}
.phase-table th{background:var(--ink);color:var(--white);font-weight:600;padding:5px 4px;text-align:left}
.phase-table td{border:1px solid #d4d5d8;padding:8px 5px;vertical-align:top;color:#333}
.phase-table .phase{color:var(--white);font-weight:700;writing-mode:vertical-rl;transform:rotate(180deg);text-align:center;width:22px;padding:4px}
.phase--green{background:var(--phase-green)}
.phase--blue{background:var(--phase-blue)}
.phase--orange{background:var(--phase-orange)}
.phase--red{background:var(--phase-red)}

/* inner right */
.why{background:var(--ink)}
.why__band{position:absolute;left:0;top:0;width:390px;height:70px;background:var(--red)}
.why__title{position:absolute;left:110px;top:18px;font-size:14px;font-weight:700;line-height:1.25;color:var(--white)}
.why__list{position:absolute;left:24px;top:90px;list-style:none;width:345px}
.why__item{display:flex;gap:12px;margin-bottom:14px}
.why__icon{flex:none;width:38px;height:38px}
.why__label{font-size:10px;font-weight:700;color:var(--red);letter-spacing:.5px}
.why__text{font-size:8px;line-height:1.45;color:var(--grey-light);margin-top:2px}
.why__photo{position:absolute;left:0;bottom:0;width:390px;height:58px;background:linear-gradient(90deg,#5b3b2c,#8a6a4e,#3b4a5a)}
</style>
</head>
<body>

<section class="spread spread--cover">
  <div class="page back-cover">
    <div class="back-cover__photo" role="img" aria-label="Photo of timber roof framing on a construction site"></div>
    <div class="back-cover__body">
      <div class="brand"><span class="brand__mark"></span><span class="brand__name">Harbison Projects</span></div>
      <p class="back-cover__contact">
        Harbison Projects Services, LLC<br>
        4820 Ledger Street, Suite 300, Dallas, TX 75201<br>
        214-555-0193<br>
        www.harbisonprojgroup.example
      </p>
    </div>
  </div>

  <div class="page front-cover">
    <svg class="front-cover__shape" width="390" height="552" viewBox="0 0 390 552">
      <defs>
        <linearGradient id="storefront" x1="0" y1="0" x2="0" y2="1">
          <stop offset="0" stop-color="#3d5a80"/>
          <stop offset=".55" stop-color="#c9a77a"/>
          <stop offset="1" stop-color="#5a3a2a"/>
        </linearGradient>
      </defs>
      <polygon points="0,250 195,185 390,250 390,552 0,552" fill="var(--red)"/>
      <polygon points="22,278 195,220 368,278 368,505 22,505" fill="url(#storefront)" role="img" aria-label="Photo of a finished restaurant storefront at dusk"/>
    </svg>
    <div class="brand front-cover__brand"><span class="brand__mark"></span><span class="brand__name">Harbison Projects</span></div>
    <p class="front-cover__web">www.harbisonprojgroup.example</p>
  </div>
</section>

<section class="spread spread--inner">
  <div class="page services">
    <div class="services__head">
      <div class="brand brand--dark"><span class="brand__mark"></span></div>
      <h2 class="services__title">Owner Representation &amp;<br>Construction Management Services</h2>
    </div>
    <table class="phase-table">
      <tr><th></th><th>Planning</th><th>Coordination</th><th>Reporting</th></tr>
      <tr><td class="phase phase--green">Pre-Design</td><td>Site review and budget set-up</td><td>Team selection and contracts</td><td>Early schedule and cost plan</td></tr>
      <tr><td class="phase phase--blue">Design</td><td>Drawing review with architect</td><td>Permit tracking and approvals</td><td>Updated estimates each phase</td></tr>
      <tr><td class="phase phase--orange">Construction</td><td>Bid review and award support</td><td>Weekly site meetings and visits</td><td>Pay request and change review</td></tr>
      <tr><td class="phase phase--red">Close-Out</td><td>Punch list and final walk</td><td>Vendor turnover and training</td><td>Final cost and warranty files</td></tr>
    </table>
  </div>

  <div class="page why">
    <div class="why__band"></div>
    <h2 class="why__title">Why Harbison Building<br>Management Group?</h2>
    <ul class="why__list">
      <li class="why__item">
        <svg class="why__icon" viewBox="0 0 38 38"><circle cx="19" cy="19" r="17" fill="none" stroke="var(--white)" stroke-width="2"/><text x="19" y="25" text-anchor="middle" font-family="Montserrat,sans-serif" font-size="17" font-weight="700" fill="var(--white)">$</text></svg>
        <div><p class="why__label">COST SAVINGS</p><p class="why__text">We protect your budget through careful planning, bidding and value review.</p></div>
      </li>
      <li class="why__item">
        <svg class="why__icon" viewBox="0 0 38 38"><path d="M5 27a14 14 0 0 1 28 0" fill="none" stroke="var(--white)" stroke-width="2"/><line x1="19" y1="27" x2="27" y2="15" stroke="var(--red)" stroke-width="2.5"/></svg>
        <div><p class="why__label">SPEED</p><p class="why__text">Clear schedules and steady oversight keep your opening date on track.</p></div>
      </li>
      <li class="why__item">
        <svg class="why__icon" viewBox="0 0 38 38"><circle cx="19" cy="19" r="17" fill="none" stroke="var(--white)" stroke-width="2"/><path d="M11 19l6 6 10-12" fill="none" stroke="var(--white)" stroke-width="2.5"/></svg>
        <div><p class="why__label">INTEGRITY</p><p class="why__text">Honest reporting and open books at every step of the project.</p></div>
      </li>
      <li class="why__item">
        <svg class="why__icon" viewBox="0 0 38 38"><rect x="5" y="8" width="28" height="18" rx="2" fill="none" stroke="var(--white)" stroke-width="2"/><line x1="13" y1="31" x2="25" y2="31" stroke="var(--white)" stroke-width="2"/></svg>
        <div><p class="why__label">TECHNOLOGY</p><p class="why__text">Modern tools give owners real-time updates on cost and progress.</p></div>
      </li>
      <li class="why__item">
        <svg class="why__icon" viewBox="0 0 38 38"><circle cx="19" cy="15" r="9" fill="none" stroke="var(--white)" stroke-width="2"/><path d="M13 22l-3 12 9-4 9 4-3-12" fill="none" stroke="var(--white)" stroke-width="2"/></svg>
        <div><p class="why__label">EXPERIENCE</p><p class="why__text">Years of restaurant and hospitality builds across many markets.</p></div>
      </li>
    </ul>
    <div class="why__photo" role="img" aria-label="Photo strip of completed restaurant interiors"></div>
  </div>
</section>

</body>
</html>
```